Website Design - for Energy Efficiency company - large corporate feel

Hi there,
Thanks for checking out this project!
We're a UK based energy efficiency business. We arrange for energy efficient systems to be fitted in people's houses (i.e. efficient boilers, solar panels etc.) However, we do not install them ourselves as we have accredited installers who install on our behalf. Therefore the website should appeal to these businesses and have a very professional corporate feel. The final design should communicate that we are a financially safe large corporation.
Our existing website should not be used for inspiration as the style and content are very outdated (it was from a time when were installers - which we no longer are).
The new website design should use the greens from our logo, however I don't want the site saturated in this colour.
I'm really open to your chosen layout and therefore I'm not a huge fan of including links to websites I like - as I don't want to limit your own creativity. However, I would like it to look corporate (but not too boring and unimaginative).
So here's a few links to websites that I feel give a feel of financially safe / large corporate etc. Although you certainly don't have to design with this style / layout in mind:
http://www.brenholt.org.uk/advice
http://www.tavishworks.co.uk/
http://www.dqvb.org.uk/
http://www.orrinlodgeway.co.uk/
http://www.pkwynd.co.uk/ (very bad design but looks corporate)
http://www.ferrowmoor.org.uk/
http://www.tq.co.uk/ (looks corporate but too busy and boring)
http://www.quellaro.co.uk/business/index.htm
http://www.mobrevo.com/
https://www.tervold.com/en/index.html
The site is for 4 different audiences:
Consumers | Businesses | Public Sector | Installers
Therefore, it's important that there is some form of way of splitting the site up into these sections (almost like 4 websites in 1). Each section will then have the navigation menu with 7 links.
I've attached our logo (company-logo.jpg) and another logo design we have to display inline with regulations (fair-loan-logo.jpg).
Happy designing, and thank you!

```html
<!DOCTYPE html>
<html lang="en">
<head>
<meta charset="utf-8">
<title>Vervane Energy</title>
<link href="https://fonts.googleapis.com/css2?family=Open+Sans:wght@300;400;600&family=Tinos&display=swap" rel="stylesheet">
<style>
:root{
  --green:#68b935;
  --green-dark:#4f9a25;
  --ink:#333;
  --muted:#8a8a8a;
  --light:#f5f5f5;
  --topbar:#3b3b3b;
  --line:#e4e4e4;
}
*{margin:0;padding:0;box-sizing:border-box}
html,body{width:814px;height:1200px;overflow:hidden}
body{position:relative;font-family:"Open Sans",sans-serif;font-weight:300;color:var(--muted);background:#fff;font-size:10px}
.abs{position:absolute}
.topbar{left:0;top:0;width:814px;height:33px;background:var(--topbar);color:#999;font-size:9.5px;line-height:33px}
.topbar .welcome{left:52px}
.topbar .call{left:478px;display:flex;align-items:center;gap:6px}
.social{display:flex;gap:11px;align-items:center}
.social span{width:9px;height:9px;border-radius:50%;background:#6a6a6a;display:block}
.topbar .social{left:622px;top:12px}
.header{left:0;top:33px;width:814px;height:65px;background:#fafafa}
.settings{left:0;top:0;width:31px;height:31px;background:var(--topbar);display:flex;align-items:center;justify-content:center}
.brand{left:52px;top:14px;font-weight:600;color:var(--green);font-size:20px;letter-spacing:-.3px;line-height:1}
.brand small{display:block;font-size:9px;color:var(--green);letter-spacing:1px;margin-top:3px;text-align:right}
.nav{left:204px;top:0;display:flex;gap:27px;height:65px;font-size:11.5px;font-weight:400;color:#555}
.nav a{color:inherit;text-decoration:none;line-height:63px;border-bottom:2px solid transparent}
.nav a.active{color:var(--green);border-color:var(--green)}
.nav a.contact{display:flex;align-items:center;gap:6px}
.searchband{left:0;top:98px;width:814px;height:64px;background:#fff}
.audiences{left:52px;top:19px;display:flex;height:26px;font-size:10px;font-weight:400;color:#666}
.audiences a{color:inherit;text-decoration:none;line-height:24px;padding:0 14px;border:1px solid #ddd;margin-right:-1px}
.audiences a.current{background:var(--green);border-color:var(--green-dark);color:#fff}
.search{left:686px;top:19px;width:77px;height:26px;border:1px solid #ddd;display:flex;align-items:center;gap:6px;padding-left:8px;color:#bbb;font-size:9px;font-style:italic}
.hero{left:0;top:162px;width:814px;height:323px;background:linear-gradient(100deg,#0e5a5a 0%,#1d8a8c 30%,#6bb8bd 55%,#c9dde3 80%,#e6eef1 100%)}
.hero-title{left:30px;top:110px;height:41px;padding:0 15px;background:rgba(40,40,40,.82);color:#fff;font-size:21px;font-weight:400;line-height:41px}
.hero-sub{left:30px;top:151px;height:30px;padding:0 13px;background:rgba(40,40,40,.82);color:#eee;font-size:11px;font-weight:400;line-height:30px}
.hero-btn{left:30px;top:189px;width:79px;height:28px;background:var(--green);color:#fff;font-size:11px;font-weight:400;display:flex;align-items:center;justify-content:center;gap:6px}
.dots{left:367px;top:296px;display:flex;gap:7px}
.dots span{width:10px;height:10px;border-radius:50%;background:rgba(60,60,60,.6)}
.dots span.on{background:var(--green)}
.tagband{left:0;top:485px;width:814px;height:83px;background:#f7f7f7;border-bottom:1px solid var(--line);text-align:center;font-family:"Tinos",serif;font-size:30px;color:#333;line-height:83px}
.card{top:600px;width:224px}
.card .photo{width:224px;height:105px;box-shadow:0 3px 0 #ececec}
.card h3{margin-top:18px;font-size:13px;font-weight:400;color:var(--ink)}
.card p{margin-top:8px;font-size:10.5px;line-height:16px;width:208px}
.card .btn{margin-top:13px;display:inline-block;width:52px;height:21px;line-height:21px;background:var(--green);color:#fff;font-size:8.5px;text-align:center;font-weight:400;border:1px solid var(--green-dark)}
.footer{left:0;top:875px;width:814px;height:272px;background:var(--light);border-top:1px solid var(--line)}
.fbrand{left:52px;top:30px;font-weight:600;color:var(--green);font-size:30px;letter-spacing:-.5px;line-height:1}
.fbrand small{display:block;font-size:13px;color:#3e6b1e;text-align:right;margin-top:6px;letter-spacing:1px}
.fabout{left:52px;top:114px;width:170px;font-size:10.5px;line-height:16px;color:#6f6f6f}
.fcol{top:33px}
.fcol h4{font-size:9.5px;font-weight:600;color:#333;letter-spacing:.5px;margin-bottom:12px}
.tweet{display:flex;gap:10px;margin-bottom:12px;font-size:10.5px;line-height:16px;color:#666}
.tweet a{color:var(--green);text-decoration:none;display:block}
.tweet em{font-size:8px;color:#888;display:block}
.thumbs{display:grid;grid-template-columns:repeat(3,44px);gap:12px 11px}
.thumbs span{height:44px;display:block;border:1px solid #fff;box-shadow:0 1px 2px rgba(0,0,0,.25)}
.info{display:flex;gap:10px;font-size:10.5px;line-height:16px;color:#666;margin-bottom:6px}
.info a{color:var(--green);text-decoration:none}
.info svg{flex:none;margin-top:3px}
.bottombar{left:0;top:1147px;width:814px;height:53px;background:var(--topbar);color:#7d7d7d;font-size:9.5px;line-height:53px}
.bottombar .copy{left:52px}
.bottombar .copy b{color:#bbb;font-weight:400}
.bottombar .follow{left:587px;display:flex;align-items:center;gap:12px}
</style>
</head>
<body>

<div class="abs topbar">
  <span class="abs welcome">Welcome to the world of Vervane Energy.</span>
  <span class="abs call">
    <svg width="9" height="9" viewBox="0 0 10 10"><path d="M2 1l2 2-1 1.3c.6 1.2 1.5 2.1 2.7 2.7L7 6l2 2-1.3 1.3C4.5 9 1 5.5.7 2.3z" fill="#888"/></svg>
    Call us: .000.000.0000
  </span>
  <div class="abs social"><span></span><span></span><span></span><span></span><span></span><span></span></div>
</div>

<div class="abs header">
  <div class="abs settings"><svg width="16" height="16" viewBox="0 0 16 16"><circle cx="8" cy="8" r="5.2" fill="none" stroke="#fff" stroke-width="3" stroke-dasharray="2.2 1.6"/><circle cx="8" cy="8" r="3" fill="#fff"/><circle cx="8" cy="8" r="1.4" fill="#3b3b3b"/></svg></div>
  <div class="abs brand">VERVANE<small>ENERGY</small></div>
  <nav class="abs nav">
    <a class="active" href="#">Home</a>
    <a href="#">About Us</a>
    <a href="#">Fair Loan</a>
    <a href="#">ECO</a>
    <a href="#">Landlords</a>
    <a href="#">Renewables</a>
    <a class="contact" href="#"><svg width="11" height="8" viewBox="0 0 11 8"><rect width="11" height="8" fill="#bbb"/><path d="M0 0l5.5 4.5L11 0" fill="none" stroke="#fff"/></svg>Contact Us</a>
  </nav>
</div>

<div class="abs searchband">
  <nav class="abs audiences" aria-label="Audience sections">
    <a class="current" href="#">Consumers</a>
    <a href="#">Businesses</a>
    <a href="#">Public Sector</a>
    <a href="#">Installers</a>
  </nav>
  <div class="abs search"><svg width="9" height="9" viewBox="0 0 10 10"><circle cx="4" cy="4" r="3" fill="none" stroke="#999" stroke-width="1.4"/><path d="M6.2 6.2L9 9" stroke="#999" stroke-width="1.6"/></svg>Search...</div>
</div>

<div class="abs hero" role="img" aria-label="Photograph of a surfer riding inside a turquoise wave with beachfront hotels in the background">
  <div class="abs hero-title">Excepteur Sint Occaecat</div>
  <div class="abs hero-sub">Nam Libero Tempore Cum Soluta Nobis Cupidatat</div>
  <div class="abs hero-btn">More <svg width="9" height="9" viewBox="0 0 10 10"><circle cx="5" cy="5" r="5" fill="#fff"/><path d="M4 2.8L6.2 5 4 7.2" fill="none" stroke="#68b935" stroke-width="1.6"/></svg></div>
  <div class="abs dots"><span></span><span></span><span class="on"></span><span></span><span></span></div>
</div>

<div class="abs tagband">"Because We Believe in Satisfaction."</div>

<div class="abs card" style="left:52px">
  <div class="photo" role="img" aria-label="Photograph of smiling colleagues looking at a tablet together" style="background:linear-gradient(120deg,#c8d4df,#9fb0c2 50%,#e7e3df)"></div>
  <h3>About Us</h3>
  <p>Excepteur sint occaecat cupidatat non proident, sunt in culpa qui officia deserunt mollit anim id est laborum.</p>
  <span class="btn">Details</span>
</div>
<div class="abs card" style="left:295px">
  <div class="photo" role="img" aria-label="Illustration of the globe surrounded by a clock, plane and clouds" style="background:radial-gradient(circle at 50% 60%,#2f6d96 0,#5a9cb8 30%,#8fc6c8 55%,#b6dcd6 100%)"></div>
  <h3>What We Do</h3>
  <p>Nemo enim ipsam voluptatem quia voluptas sit aspernatur aut odit aut fugit, sed quia consequuntur magni dolores.</p>
  <span class="btn">Details</span>
</div>
<div class="abs card" style="left:538px">
  <div class="photo" role="img" aria-label="Photograph of a glass office building facade" style="background:linear-gradient(160deg,#1f4e84,#4f86bd 50%,#a9c9e6)"></div>
  <h3>Recent Work</h3>
  <p>Neque porro quisquam est, qui dolorem ipsum quia dolor sit amet, consectetur, adipisci velit, sed quia non.</p>
  <span class="btn">Details</span>
</div>

<footer class="abs footer">
  <div class="abs fbrand">VERVANE<small>ENERGY</small></div>
  <p class="abs fabout">Duis autem vel eum iriure dolor in hendrerit in vulputate velit esse molestie consequat, vel illum dolore eu feugiat nulla facilisis at vero eros et accumsan et iusto odio dignissim qui</p>

  <div class="abs fcol" style="left:235px;width:160px">
    <h4>LATEST TWEETS</h4>
    <div class="tweet"><svg width="10" height="9" viewBox="0 0 10 9"><path d="M1 2l3 2 5-3-3 6-2-2z" fill="#bbb"/></svg><div>Sed ut perspiciatis unde omnis iste natus error sit voluptatem<a href="#">http://chirpline.net</a><em>Jan 7, 2013</em></div></div>
    <div class="tweet"><svg width="10" height="9" viewBox="0 0 10 9"><path d="M1 2l3 2 5-3-3 6-2-2z" fill="#bbb"/></svg><div>Nemo enim ipsam voluptatem quia voluptas sit aspernatur aliquid :)<a href="#">http://chirpline.net</a><em>Jan 7, 2013</em></div></div>
  </div>

  <div class="abs fcol" style="left:417px">
    <h4>LATEST PROJECTS</h4>
    <div class="thumbs">
      <span role="img" aria-label="Mountain lake landscape" style="background:linear-gradient(#8a8f96,#4a4c47)"></span>
      <span role="img" aria-label="Green mountain valley" style="background:linear-gradient(#7a9aa8,#3c5a3a)"></span>
      <span role="img" aria-label="Sunset over a river valley" style="background:linear-gradient(#d08a3c,#3a2f25)"></span>
      <span role="img" aria-label="Mountain meadow at dusk" style="background:linear-gradient(#6a6f7a,#5a6a2a)"></span>
      <span role="img" aria-label="Hazy blue hills" style="background:linear-gradient(#7fa3b8,#27404f)"></span>
      <span role="img" aria-label="Green terraced hillside" style="background:linear-gradient(#9cc0a0,#3f6b25)"></span>
    </div>
  </div>

  <div class="abs fcol" style="left:600px;width:165px">
    <h4>CONTACT INFORMATION</h4>
    <div class="info"><svg width="8" height="10" viewBox="0 0 8 10"><path d="M4 0a4 4 0 014 4c0 3-4 6-4 6S0 7 0 4a4 4 0 014-4z" fill="#bbb"/><circle cx="4" cy="4" r="1.5" fill="#f5f5f5"/></svg><span>103088. Ut wisi enim ad minim veniam, quis nostrud.</span></div>
    <div class="info"><svg width="10" height="8" viewBox="0 0 10 8"><rect width="10" height="8" fill="#bbb"/><path d="M0 0l5 4 5-4" fill="none" stroke="#f5f5f5"/></svg><a href="#">mail@vervane.co.uk</a></div>
    <div class="info"><svg width="9" height="9" viewBox="0 0 10 10"><path d="M2 1l2 2-1 1.3c.6 1.2 1.5 2.1 2.7 2.7L7 6l2 2-1.3 1.3C4.5 9 1 5.5.7 2.3z" fill="#bbb"/></svg><span>+44 (20) 7946-03-21</span></div>
    <div class="info"><svg width="9" height="9" viewBox="0 0 10 10"><circle cx="5" cy="5" r="4.3" fill="none" stroke="#bbb" stroke-width="1.2"/><path d="M5 2.5V5h2" fill="none" stroke="#bbb"/></svg><span>Monday-Friday: 9:00 — 18:00<br>Saturday: 10:00 — 17:00<br>Sunday: closed</span></div>
  </div>
</footer>

<div class="abs bottombar">
  <span class="abs copy">Copyright © 2013 <b>Vervane Energy</b>. All Right Reserved.</span>
  <div class="abs follow">Follow Us: <div class="social"><span></span><span></span><span></span><span></span><span></span></div></div>
</div>

</body>
</html>
```